Building company business card

Design and print business cards for BRENTHOLM PTY LTD.
A residantial homes building company.
Mark Lantern already designed the company Logo.

```html
<!DOCTYPE html>
<html lang="en">
<head>
<meta charset="utf-8">
<title>BRENTHOLM PTY LTD – Business Card</title>
<link href="https://fonts.googleapis.com/css2?family=Carlito:wght@400;700&display=swap" rel="stylesheet">
<style>
  :root {
    --stage: #ababab;
    --navy: #162466;
    --gold: #b88a2e;
    --white: #ffffff;
  }
  * { margin: 0; padding: 0; box-sizing: border-box; }
  html, body {
    width: 1200px; height: 1000px; overflow: hidden;
    background: var(--stage);
    font-family: "Carlito", "Calibri", sans-serif;
  }
  .card {
    position: absolute;
    left: 294px;
    width: 613px; height: 352px;
    border-radius: 24px;
    overflow: hidden;
  }
  .card-front {
    top: 123px;
    background: var(--navy);
    display: flex; align-items: center; justify-content: center;
  }
  .front-brand {
    display: flex; align-items: center; gap: 14px;
    color: var(--gold);
    font-weight: 700; font-size: 40px; letter-spacing: 2px;
  }
  .brand-square {
    width: 26px; height: 26px; background: var(--gold);
  }
  .card-back {
    top: 530px;
    background: var(--white);
    color: var(--navy);
  }
  .back-brand {
    position: absolute; left: 59px; top: 70px;
    display: flex; align-items: center; gap: 12px;
    font-weight: 700; font-size: 38px; letter-spacing: 1px;
    color: var(--navy);
  }
  .back-brand .brand-square { width: 30px; height: 30px; }
  .person-name {
    position: absolute; left: 59px; top: 146px;
    font-weight: 700; font-size: 21px;
  }
  .person-role {
    position: absolute; left: 59px; top: 168px;
    font-weight: 700; font-size: 16px; color: var(--gold);
  }
  .address {
    position: absolute; left: 61px; top: 196px;
    font-size: 16.5px; line-height: 22px;
  }
  .contacts {
    position: absolute; left: 59px; top: 249px;
    list-style: none; font-size: 16.5px; line-height: 22px;
  }
  .contacts li { display: flex; align-items: center; gap: 6px; }
  .contacts svg { width: 14px; height: 14px; fill: var(--gold); flex: none; }
</style>
</head>
<body>
  <section class="card card-front">
    <div class="front-brand"><span class="brand-square"></span>BRENTHOLM</div>
  </section>

  <section class="card card-back">
    <div class="back-brand"><span class="brand-square"></span>BRENTHOLM</div>
    <h1 class="person-name">DAMIANOS (Dan) KORRAS</h1>
    <p class="person-role">Director</p>
    <address class="address" style="font-style:normal">
      CDB-U 51846, PO Box 208<br>
      Kelmere East, Vic 3190
    </address>
    <ul class="contacts">
      <li>
        <svg viewBox="0 0 14 14" aria-hidden="true"><path d="M3.5 0h7v14h-7z M4.8 1.4v9.8h4.4V1.4z M6.3 12h1.4v1.2H6.3z" fill-rule="evenodd"/></svg>
        0400 123 456
      </li>
      <li>
        <svg viewBox="0 0 14 14" aria-hidden="true"><path d="M3 1l2.4 2.6-1.2 1.8c.9 1.9 2.4 3.4 4.3 4.3l1.8-1.2L13 11l-1.6 2C6 12.6 1.4 8 1 2.6z"/></svg>
        0455 010 203
      </li>
      <li>
        <svg viewBox="0 0 14 14" aria-hidden="true"><path d="M0 3h14v8.5H0z M0 3l7 5 7-5" fill-rule="evenodd"/><path d="M0.5 3.3L7 8l6.5-4.7" stroke="#fff" stroke-width="1" fill="none"/></svg>
        dk@brentholm-pl.com
      </li>
    </ul>
  </section>
</body>
</html>
```